Tri-fold Brochure Design for Banking Business

The brochure we have needs to be improved - more business like and more attractive. Logo file and brochure is attached. I would like to be able to edit the text after you get done. Your ideas and changes to text are welcome. See our website www.korvanbridgegrp.com for our theme. We can use indesign to edit the text after you complete. However, please make changes to the text we have in the design that it uploaded. Your comments and changes are welcome.

Target Market(s)

Human Resources and learning & development staff at the global investment banks - Pellham Trask, QWNR, etc.

Industry/Entity Type

Investment Banking

Logo Text

Korvan Bridge Group

Font styles to use
Serif
Sans Serif

Colors
33a6d7
0493ce
3277b5
fbf289
fdf9cf
fbee3e
0555a3
85acd3

Requirements
Must have
• Must be similar to our website www.korvanbridgegrp.com. Needs to be business-like, clean fonts, sharp design. Our logo - of course.
Nice to have
• City images - seems to be our theme.

```html
<!DOCTYPE html>
<html lang="en">
<head>
<meta charset="utf-8">
<title>Korvan Bridge Group – Tri-fold Brochure</title>
<link href="https://fonts.googleapis.com/css2?family=Nunito+Sans:wght@300;400;700;800&display=swap" rel="stylesheet">
<style>
:root{
  --sky:#33a6d7;
  --azure:#0493ce;
  --steel:#3277b5;
  --navy:#0555a3;
  --mist:#85acd3;
  --ink:#1d2530;
  --paper:#ffffff;
  --bg:#d6d6d6;
  --deep:#0b2b55;
}
*{box-sizing:border-box;margin:0;padding:0}
html,body{width:1200px;height:1200px;overflow:hidden;background:var(--bg);font-family:"Nunito Sans",sans-serif;color:var(--ink)}
.sheet{position:absolute;left:263px;width:696px;height:491px;background:var(--paper);overflow:hidden}
.sheet.outside{top:45px}
.sheet.inside{top:597px}
.panel{position:absolute;top:0;width:232px;height:491px;overflow:hidden}
.p1{left:0}.p2{left:232px}.p3{left:464px}
.shade{background:linear-gradient(90deg,#e2e2e2 0%,#fff 35%,#fff 100%)}
.tab{position:absolute;left:24px;width:184px;background:var(--sky);color:#fff;font-weight:300;text-transform:uppercase;font-size:16px;letter-spacing:.3px;text-align:center;display:flex;align-items:flex-end;justify-content:center;padding-bottom:7px;line-height:1.1}
.copy{position:absolute;left:26px;width:184px;font-size:8px;line-height:1.22;color:#222}
.copy p{margin-bottom:9px}
.photo{position:absolute;left:0;width:232px}
.heading{position:absolute;left:0;width:232px;text-align:center;color:var(--navy);font-weight:300;text-transform:uppercase;font-size:16px}
.band{position:absolute;left:0;width:232px;background:var(--sky);color:#fff}
.region{font-size:7px;font-weight:700;color:var(--navy);text-align:center;margin-top:10px;letter-spacing:.3px}
.mail{font-size:8px;text-align:center;margin-top:3px}
.contact-list{position:relative;z-index:1}
.contact-row{display:flex;gap:9px;align-items:flex-start;margin:0 0 11px 26px;font-size:7.6px;line-height:1.2}
.contact-row svg{flex:0 0 10px;margin-top:1px}
.emblem-area{position:absolute;left:0;top:104px;width:232px;height:126px;background:linear-gradient(135deg,var(--sky) 0%,var(--sky) 45%,#1a74bf 70%,var(--navy) 100%)}
.service-name{position:absolute;left:0;top:186px;width:232px;text-align:center;font-weight:800;font-size:11.5px;color:#fff;z-index:1}
.brand{position:absolute;left:21px;top:330px;width:186px;height:59px;background:var(--sky);display:flex;align-items:center;justify-content:center;gap:7px}
.brand-mark{width:8px;height:8px;background:var(--deep)}
.brand-name{font-weight:800;font-size:12px;letter-spacing:.3px;color:var(--deep);white-space:nowrap}
.tagline{position:absolute;left:0;width:232px;top:416px;text-align:center;color:var(--navy);font-weight:800;font-size:11px;line-height:1.25}
.urlbar{position:absolute;left:21px;top:460px;width:186px;height:31px;background:var(--sky);color:#fff;font-size:8px;text-align:center;padding-top:13px}
.ticks{list-style:none;position:absolute;left:24px;top:162px;width:190px;font-size:7.8px;line-height:1.2}
.ticks li{display:flex;gap:8px;margin-bottom:13px}
.ticks svg{flex:0 0 9px;margin-top:1px}
.team-box{position:absolute;left:21px;top:267px;width:186px;height:106px;background:var(--sky);color:#fff;font-size:8px;line-height:1.22;padding:15px 12px 0 11px;z-index:2}
.team-box p{margin-bottom:9px}
</style>
</head>
<body>

<section class="sheet outside">
  <div class="panel p1 shade">
    <div class="tab" style="top:0;height:51px">About Us</div>
    <div class="copy" style="top:74px">
      <p>Korvan Bridge Group efficiently provides complete efficiently provides complete sales, marketing and logistical support for all our programs, no matter the location.</p>
      <p>Our globally located trainers have extensive experience, both as industry professionals and as trainers.</p>
      <p>Our highly qualified logistical team compliment the training services, providing reliable and efficient support.</p>
    </div>
    <div class="photo" style="top:200px;height:291px;background:linear-gradient(180deg,#d8d4c6 0%,#9aa7ad 35%,#4e6475 65%,#24394b 100%)" role="img" aria-label="City skyline with a glass spire tower beside a river at dusk"></div>
  </div>

  <div class="panel p2">
    <div class="heading" style="top:24px">Get in Touch</div>
    <div class="band" style="top:51px;height:149px;padding-top:8px">
      <div class="region">GLOBAL</div>
      <div class="mail">elena.varga@korvanbridgegrp.com</div>
      <div class="region">ASIA</div>
      <div class="mail">paul.hendry@korvanbridgegrp.com</div>
      <div class="region">UNITED STATES</div>
      <div class="mail">james.corvel@korvanbridgegrp.com</div>
      <div class="region">EUROPE</div>
      <div class="mail">simon.draper@korvanbridgegrp.com</div>
    </div>
    <div class="heading" style="top:221px">Contact Us</div>
    <div class="band" style="top:261px;height:230px;padding-top:23px">
      <div class="emblem-area" role="img" aria-label="Globe network emblem with a long diagonal shadow"></div>
      <div class="contact-list">
        <div class="contact-row"><svg width="10" height="10" viewBox="0 0 10 10"><path d="M2 0.5 L3.6 2.6 L2.7 3.7 Q3.8 6 6.2 7.2 L7.3 6.3 L9.5 7.9 L8.3 9.5 Q1.5 8.3 0.5 1.6Z" fill="#0b4c94"/></svg><span>+852 2730 4186</span></div>
        <div class="contact-row"><svg width="10" height="8" viewBox="0 0 10 8"><rect x="0" y="0.5" width="10" height="7" fill="#0b4c94"/><path d="M0 .5 L5 4.5 L10 .5" stroke="#33a6d7" fill="none"/></svg><span>info@korvanbridgegrp.com</span></div>
        <div class="contact-row"><svg width="10" height="12" viewBox="0 0 10 12"><path d="M5 0 A4.5 4.5 0 0 1 9.5 4.5 C9.5 7.5 5 12 5 12 C5 12 .5 7.5 .5 4.5 A4.5 4.5 0 0 1 5 0Z" fill="#0b4c94"/><circle cx="5" cy="4.5" r="1.7" fill="#33a6d7"/></svg><span>Flat 6B Lanford Trade Building<br>412-418 Harbour Rd, Eastpoint</span></div>
      </div>
      <div class="service-name">Worldwide Training Service</div>
    </div>
  </div>

  <div class="panel p3 shade">
    <div class="photo" style="top:0;height:359px;background:linear-gradient(180deg,#a9c6df 0%,#8aa9c2 40%,#5b7690 70%,#3e5a72 100%)" role="img" aria-label="Harbour skyline with a tall glass tower under a cloudy sky"></div>
    <div class="brand"><span class="brand-mark"></span><span class="brand-name">KORVAN BRIDGE GROUP</span></div>
    <div class="tagline">YOUR EXPERT TRAINING &amp;<br>CONSULTING PARTNER</div>
    <div class="urlbar">www.korvanbridgegrp.com</div>
  </div>
</section>

<section class="sheet inside">
  <div class="panel p1 shade">
    <div class="tab" style="top:0;height:58px">Why Choose Us ?</div>
    <div class="copy" style="top:78px">
      <p>Korvan Bridge Group is dedicated to providing you and your firm with the highest level of service.</p>
      <p>We provide dedicated sales and logistics support for each program to insure consistent, reliable results.</p>
    </div>
    <ul class="ticks">
      <li><svg width="9" height="8" viewBox="0 0 9 8"><polygon points="4.5,.5 8.5,7.5 .5,7.5" fill="none" stroke="#0555a3" stroke-width="1.3"/></svg><span>Highly qualified,international pool of trainers</span></li>
      <li><svg width="9" height="8" viewBox="0 0 9 8"><polygon points="4.5,.5 8.5,7.5 .5,7.5" fill="none" stroke="#0555a3" stroke-width="1.3"/></svg><span>Strong client relationship management and support</span></li>
      <li><svg width="9" height="8" viewBox="0 0 9 8"><polygon points="4.5,.5 8.5,7.5 .5,7.5" fill="none" stroke="#0555a3" stroke-width="1.3"/></svg><span>Competitive pricing and flexibility</span></li>
      <li style="margin-top:6px"><svg width="9" height="8" viewBox="0 0 9 8"><polygon points="4.5,.5 8.5,7.5 .5,7.5" fill="none" stroke="#0555a3" stroke-width="1.3"/></svg><span>Outcome driven approach directly matches your company's needs</span></li>
    </ul>
    <div class="photo" style="top:283px;height:208px;background:radial-gradient(circle at 45% 35%,#dff1ff 0%,#4f7aa6 18%,#1d3b63 55%,#0f2340 100%)" role="img" aria-label="Hanging light bulbs with one glowing bulb on a dark blue background"></div>
  </div>

  <div class="panel p2 shade">
    <div class="photo" style="top:0;height:205px;background:linear-gradient(160deg,#4a78a6 0%,#7fa8cf 40%,#3c6894 100%)" role="img" aria-label="Businessman touching a digital interface of training, mentoring and skill keywords"></div>
    <div class="tab" style="top:175px;left:23px;height:59px;width:185px;padding-bottom:9px">Our Services</div>
    <div class="copy" style="top:256px;left:23px;width:190px;font-size:7.8px">
      <p>Korvan Bridge Group provides best in class services for all our clients.</p>
      <p style="margin-top:14px">We provide highly customized programs tailored to your specific requirements.</p>
      <p style="margin-top:14px">Direct interaction between our clients, consulting trainers and client service staff ensures measurable outcomes for program participants.</p>
      <p style="margin-top:14px">We facilitate learning outcomes using a blended methodology combining interactive analysis, hands-on experiential models, market simulations and a state-of-the-art learning management system.</p>
      <p style="margin-top:14px">Our material databanks are continuously updated to insure accuracy and effectiveness of our services.</p>
    </div>
  </div>

  <div class="panel p3">
    <div class="tab" style="left:21px;width:186px;top:0;height:58px;padding-bottom:6px">Marketing<br>Similutions</div>
    <div class="copy" style="top:82px;left:21px;width:188px;font-size:7.8px;line-height:1.24">
      <p>Korvan Bridge has partnered with Vantrel as our technology provider for simulations. These simulations are built to be a mirror of reality yet provide significant educational value. Simulations add a competitive element to programs by providing an engaging, interactive environment. Vantrel simulations allow realistic interaction with real market data giving program participants the opportunity to experience different market scenarios and implement different strategies.</p>
    </div>
    <div class="heading" style="top:231px">Our Team</div>
    <div class="team-box">
      <p>Our Consulting Trainers are located globally and recognized by the industry as highly effective trainers and program facilitators.</p>
      <p>Korvan provides global expertise for our programs with local talent for program facilitation.</p>
    </div>
    <div class="photo" style="top:337px;height:154px;background:linear-gradient(180deg,#cfe0ee 0%,#8fb3d4 45%,#3f6c98 100%)" role="img" aria-label="Group of business people standing in a circle on top of the globe"></div>
  </div>
</section>

</body>
</html>
```